Healing stone/crystal Shopify store

Hi - I'm creating a new site to sell healing crystals/stones.Name for the shop is MoonpetalHaven. Site helps people to choose best crystals for them .Shop should have blog aswell.The site should be informative and attractive. Stones we sell Opalite,Green Aventurine,Watermelon Crystal,Rose Quartz Stone,Tiger Eye Stone. Must be Shopify. No content yet, you can fill neccessary fields Lorea Ipsum and if you have some good idea you can put it there
Updates

Designs look the same

Target Market(s)

Woman, English speaking countries.

Industry/Entity Type

Shop

Number of Pages Required

1 page

Colors

Designer to choose colors to be used in the design.

Requirements
Must have
• Blog
Nice to have
• High quality pictures to look site attractive.

```html
<!DOCTYPE html>
<html lang="en">
<head>
<meta charset="utf-8">
<title>MoonpetalHaven – Healing Crystals</title>
<link rel="stylesheet" href="https://fonts.googleapis.com/css2?family=Poppins:ital,wght@0,300;0,400;0,500;0,600;0,800;1,400;1,600;1,700&family=Open+Sans:wght@400;600&display=swap">
<style>
:root{
  --accent:#c2500f;
  --cocoa:#4a342e;
  --ink:#1d1d1d;
  --text:#555;
  --line:#d6d6d6;
  --paper:#ffffff;
  --night:#2a2a2d;
  --placeholder:#e4e1df;
}
*{box-sizing:border-box;margin:0;padding:0}
html,body{width:1200px;height:4511px;overflow:hidden;background:var(--paper)}
body{position:relative;font-family:"Open Sans",Arial,sans-serif;color:var(--text)}
.abs{position:absolute}

/* header */
.site-header{left:0;top:0;width:1200px;height:84px;background:var(--paper)}
.brand{left:48px;top:18px;font-family:"Poppins",Arial,sans-serif;font-weight:600;font-size:32px;color:var(--ink);display:flex;align-items:center;gap:12px}
.brand-dot{width:14px;height:14px;border-radius:50%;background:var(--ink)}
.search-icon{left:912px;top:25px}
.currency{left:955px;top:22px;width:80px;height:38px;background:#d4d4d4;border-radius:3px;font:500 15px "Poppins",sans-serif;color:#333;display:flex;align-items:center;justify-content:center;gap:8px}
.cart{left:1060px;top:22px;width:92px;height:38px;background:#d4d4d4;border-radius:3px;font:500 15px "Poppins",sans-serif;color:#333;display:flex;align-items:center;justify-content:center;gap:8px}

/* hero */
.hero{left:0;top:84px;width:1200px;height:732px;background:linear-gradient(100deg,#b9c6da 0%,#8796aa 30%,#7b8f86 60%,#9fb8a4 80%,#cfa8a6 100%);overflow:hidden}
.hero-shade{left:0;top:0;width:1200px;height:732px;background:rgba(0,0,0,.28)}
.hero-title{left:0;top:228px;width:1200px;text-align:center;font:400 70px/88px "Poppins",sans-serif;color:#fff;text-shadow:0 2px 8px rgba(0,0,0,.35)}
.hero-btn{left:520px;top:431px;width:160px;height:50px;border:2px solid #fff;background:rgba(0,0,0,.55);color:#fff;font:500 17px/46px "Poppins",sans-serif;text-align:center;letter-spacing:.5px}
.hero-arrow{top:316px;width:112px;height:172px;background:rgba(20,20,20,.7);display:flex;align-items:center;justify-content:center}
.hero-dots{left:480px;top:692px;display:flex;gap:10px}
.hero-dots span{width:70px;height:8px;background:rgba(255,255,255,.55)}
.hero-dots span.on{background:#fff}

/* collection */
.section-title{font:400 38px "Poppins",sans-serif;color:var(--ink)}
.row-arrow{width:38px;height:38px;background:var(--ink);display:flex;align-items:center;justify-content:center}
.card{width:225px;text-align:center}
.card-img{position:relative;width:190px;height:130px;margin:10px auto 0;border-radius:6px}
.sale{position:absolute;top:-28px;right:-10px;width:54px;height:38px;background:var(--accent);color:#fff;font:700 15px/38px "Poppins",sans-serif;text-align:center}
.quick{position:absolute;bottom:-34px;left:0;width:190px;height:28px;background:var(--accent);color:#fff;font:600 14px/28px "Poppins",sans-serif;letter-spacing:.4px}
.card-name{margin-top:42px;font:400 17px "Poppins",sans-serif;color:#666}
.card-name.hot{color:var(--accent)}
.card-stars{margin-top:6px;font-size:15px;color:#111;letter-spacing:1px}
.card-stars small{font-size:12px;color:#888;letter-spacing:0;margin-left:4px}
.card-price{margin-top:4px;font-size:12px;color:#555}

/* newsletter */
.newsletter{left:0;top:1995px;width:1200px;height:330px;background:var(--cocoa);text-align:center;color:#fff}
.newsletter h2{margin-top:76px;font:italic 600 34px "Poppins",sans-serif}
.newsletter p{margin:10px auto 0;width:1040px;font:italic 500 15px/25px "Poppins",sans-serif}
.signup{display:flex;justify-content:center;gap:14px;margin-top:32px}
.signup .field{width:200px;height:30px;background:#c8c8c8;color:#555;font-size:13px;line-height:30px;text-align:left;padding-left:10px}
.signup .go{width:90px;height:30px;background:var(--accent);font:600 15px/30px "Poppins",sans-serif}

/* product detail */
.feature-img{left:60px;top:2420px;width:495px;height:490px;background:linear-gradient(160deg,#3e4a8a,#232a5a);border-radius:6px}
.thumb{top:3032px;width:90px;height:82px;border-radius:6px}
.detail{left:648px;top:2427px;width:501px}
.detail .rule{height:1px;background:var(--line)}
.detail .name{font:400 24px/64px "Poppins",sans-serif;color:#666}
.detail .reviews{margin-top:14px;font-size:15px;color:#555}
.detail .reviews b{color:#444;letter-spacing:1px;font-weight:400}
.detail .price{margin-top:10px;font:italic 700 32px "Poppins",sans-serif;color:var(--accent)}
.detail .copy{margin-top:34px;font-size:13.5px;line-height:23px;color:#555}
.detail .copy p+p{margin-top:22px}
.add-cart{left:648px;top:3066px;width:501px;height:60px;background:var(--accent);color:#fff;font:800 34px/60px "Poppins",sans-serif;text-align:center;letter-spacing:.5px}

/* blog */
.blog-rule{left:48px;top:3292px;width:1104px;height:1px;background:var(--line)}
.post{top:3315px;width:351px}
.post-img{width:351px;height:272px;background:var(--placeholder)}
.post h3{margin-top:34px;font:600 17px "Poppins",sans-serif;color:var(--accent)}
.post .date{margin-top:4px;font-size:10px;color:#999}
.post .excerpt{margin-top:10px;font-size:10.5px;line-height:16px;color:#666}

/* testimonials */
.testimonials{left:0;top:3858px;width:1200px;height:404px;background:linear-gradient(90deg,#4a3c30 0%,#333336 35%,#38393c 65%,#55595f 100%)}
.testimonials h2{position:absolute;left:0;top:56px;width:1200px;text-align:center;font:400 40px "Poppins",sans-serif;color:#fff}
.quote-box{left:180px;top:4000px;width:840px;height:178px;background:rgba(150,150,150,.5);text-align:center;color:#fff;font-size:14px;line-height:22px;padding-top:34px}
.quote-box .who{margin-top:18px;font-size:12px}
.t-arrow{top:4200px;width:40px;height:40px;background:var(--accent);display:flex;align-items:center;justify-content:center}

/* footer */
.footer{left:0;top:4403px;width:1200px;text-align:center;font:600 17px "Poppins",sans-serif;color:var(--ink)}
.footer span{color:var(--accent)}
</style>
</head>
<body>

<header class="site-header abs">
  <div class="brand abs"><span class="brand-dot"></span>MoonpetalHaven</div>
  <svg class="search-icon abs" width="28" height="30" viewBox="0 0 28 30"><circle cx="11" cy="11" r="8" fill="none" stroke="#222" stroke-width="3"/><line x1="17" y1="17" x2="25" y2="26" stroke="#222" stroke-width="3.5" stroke-linecap="round"/></svg>
  <div class="currency abs">USD <svg width="12" height="8" viewBox="0 0 12 8"><path d="M0 0h12L6 8z" fill="#333"/></svg></div>
  <div class="cart abs"><svg width="18" height="16" viewBox="0 0 18 16"><path d="M1 1h3l2 9h9l2-6H5" fill="none" stroke="#333" stroke-width="1.8"/><circle cx="7" cy="14" r="1.5" fill="#333"/><circle cx="14" cy="14" r="1.5" fill="#333"/></svg>Cart</div>
</header>

<section class="hero abs" role="img" aria-label="Photo of carved crystal angel figurines in opalite, green aventurine, rose quartz and clear quartz">
  <div class="hero-shade abs"></div>
  <h1 class="hero-title abs">Sample Text Here<br>Sample text</h1>
  <div class="hero-btn abs">SHOP NOW</div>
  <div class="hero-arrow abs" style="left:0"><svg width="36" height="60" viewBox="0 0 36 60"><path d="M30 4L6 30l24 26" fill="none" stroke="#fff" stroke-width="5"/></svg></div>
  <div class="hero-arrow abs" style="left:1088px"><svg width="36" height="60" viewBox="0 0 36 60"><path d="M6 4l24 26L6 56" fill="none" stroke="#fff" stroke-width="5"/></svg></div>
  <div class="hero-dots abs"><span></span><span class="on"></span><span class="on"></span></div>
</section>

<h2 class="section-title abs" style="left:48px;top:860px">Crystal Collection</h2>

<div class="row-arrow abs" style="left:0;top:1061px"><svg width="14" height="20"><path d="M12 2L3 10l9 8" fill="none" stroke="#fff" stroke-width="3"/></svg></div>
<div class="row-arrow abs" style="left:1162px;top:1061px"><svg width="14" height="20"><path d="M2 2l9 8-9 8" fill="none" stroke="#fff" stroke-width="3"/></svg></div>
<div class="row-arrow abs" style="left:0;top:1382px"><svg width="14" height="20"><path d="M12 2L3 10l9 8" fill="none" stroke="#fff" stroke-width="3"/></svg></div>
<div class="row-arrow abs" style="left:1162px;top:1382px"><svg width="14" height="20"><path d="M2 2l9 8-9 8" fill="none" stroke="#fff" stroke-width="3"/></svg></div>
<div class="row-arrow abs" style="left:0;top:1706px"><svg width="14" height="20"><path d="M12 2L3 10l9 8" fill="none" stroke="#fff" stroke-width="3"/></svg></div>
<div class="row-arrow abs" style="left:1162px;top:1706px"><svg width="14" height="20"><path d="M2 2l9 8-9 8" fill="none" stroke="#fff" stroke-width="3"/></svg></div>

<!-- row 1 -->
<div class="card abs" style="left:38px;top:1000px"><div class="card-img" role="img" aria-label="Photo of a watermelon crystal elephant carving" style="background:linear-gradient(160deg,#f3c3c7,#e58a92)"><span class="sale">SALE</span></div><div class="card-name">Sample Name Here</div><div class="card-stars">★★★★★<small>2 Reviews</small></div><div class="card-price">$49.00</div></div>
<div class="card abs" style="left:263px;top:1000px"><div class="card-img" role="img" aria-label="Photo of a rose quartz elephant carving" style="background:linear-gradient(160deg,#f7d6e6,#e9aecb)"><span class="quick">+ QUICK SHOP</span></div><div class="card-name hot">Sample Name Here</div><div class="card-stars" style="color:var(--accent)">★★★★★<small>2 Reviews</small></div><div class="card-price" style="color:var(--accent)">$49.00</div></div>
<div class="card abs" style="left:488px;top:1000px"><div class="card-img" role="img" aria-label="Photo of an opalite elephant carving" style="background:linear-gradient(160deg,#f2f5fa,#d6deec)"></div><div class="card-name">Sample Name Here</div><div class="card-stars">★★★★★<small>2 Reviews</small></div><div class="card-price">$49.00</div></div>
<div class="card abs" style="left:713px;top:1000px"><div class="card-img" role="img" aria-label="Photo of a green aventurine elephant carving" style="background:linear-gradient(160deg,#d3eada,#a8d0b2)"><span class="sale">SALE</span></div><div class="card-name">Sample Name Here</div><div class="card-stars">★★★★★<small>2 Reviews</small></div><div class="card-price">$49.00</div></div>
<div class="card abs" style="left:938px;top:1000px"><div class="card-img" role="img" aria-label="Photo of a tiger eye elephant carving" style="background:linear-gradient(160deg,#b48c66,#7a5a3e)"></div><div class="card-name">Sample Name Here</div><div class="card-stars">★★★★★<small>2 Reviews</small></div><div class="card-price">$49.00</div></div>

<!-- row 2 -->
<div class="card abs" style="left:38px;top:1328px"><div class="card-img" role="img" aria-label="Photo of green aventurine elephant carvings" style="background:linear-gradient(160deg,#b7d4ba,#7fa888)"></div><div class="card-name">Sample Name Here</div><div class="card-stars">★★★★★<small>2 Reviews</small></div><div class="card-price">$49.00</div></div>
<div class="card abs" style="left:263px;top:1328px"><div class="card-img" role="img" aria-label="Photo of tiger eye elephant carvings" style="background:linear-gradient(160deg,#a88565,#6a5040)"><span class="sale">SALE</span></div><div class="card-name">Sample Name Here</div><div class="card-stars">★★★★★<small>2 Reviews</small></div><div class="card-price">$49.00</div></div>
<div class="card abs" style="left:488px;top:1328px"><div class="card-img" role="img" aria-label="Photo of watermelon crystal elephant carvings" style="background:linear-gradient(160deg,#f1bcc0,#e0848c)"></div><div class="card-name">Sample Name Here</div><div class="card-stars">★★★★★<small>2 Reviews</small></div><div class="card-price">$49.00</div></div>
<div class="card abs" style="left:713px;top:1328px"><div class="card-img" role="img" aria-label="Photo of opalite elephant carvings" style="background:linear-gradient(160deg,#f4f6fa,#d9e1ee)"></div><div class="card-name">Sample Name Here</div><div class="card-stars">★★★★★<small>2 Reviews</small></div><div class="card-price">$49.00</div></div>
<div class="card abs" style="left:938px;top:1328px"><div class="card-img" role="img" aria-label="Photo of amethyst elephant carvings" style="background:linear-gradient(160deg,#ead4ee,#c9a2d2)"><span class="sale">SALE</span></div><div class="card-name">Sample Name Here</div><div class="card-stars">★★★★★<small>2 Reviews</small></div><div class="card-price">$49.00</div></div>

<!-- row 3 -->
<div class="card abs" style="left:38px;top:1656px"><div class="card-img" role="img" aria-label="Photo of a clear quartz angel carving" style="background:linear-gradient(160deg,#f6f6f6,#dadada)"><span class="sale">SALE</span></div><div class="card-name">Sample Name Here</div><div class="card-stars">★★★★★<small>2 Reviews</small></div><div class="card-price">$49.00</div></div>
<div class="card abs" style="left:263px;top:1656px"><div class="card-img" role="img" aria-label="Photo of a rose quartz angel carving" style="background:linear-gradient(160deg,#f8dde0,#ecb6be)"></div><div class="card-name">Sample Name Here</div><div class="card-stars">★★★★★<small>2 Reviews</small></div><div class="card-price">$49.00</div></div>
<div class="card abs" style="left:488px;top:1656px"><div class="card-img" role="img" aria-label="Photo of a sodalite angel carving" style="background:linear-gradient(160deg,#6c74a8,#3a4078)"></div><div class="card-name">Sample Name Here</div><div class="card-stars">★★★★★<small>2 Reviews</small></div><div class="card-price">$49.00</div></div>
<div class="card abs" style="left:713px;top:1656px"><div class="card-img" role="img" aria-label="Photo of a tiger eye angel carving" style="background:linear-gradient(160deg,#d8b27e,#a8804c)"></div><div class="card-name">Sample Name Here</div><div class="card-stars">★★★★★<small>2 Reviews</small></div><div class="card-price">$49.00</div></div>
<div class="card abs" style="left:938px;top:1656px"><div class="card-img" role="img" aria-label="Photo of an amethyst angel carving" style="background:linear-gradient(160deg,#e0cdee,#b79ad2)"><span class="sale">SALE</span></div><div class="card-name">Sample Name Here</div><div class="card-stars">★★★★★<small>2 Reviews</small></div><div class="card-price">$49.00</div></div>

<section class="newsletter abs">
  <h2>Get news + discounts delivered monthly!</h2>
  <p>Lorem ipsum dolor sit amet, consectetur adipisicing elit. Provident, rem ut ab odio nemo sapiente obcaecati praesentium laboriosam tempore quas quaerat, animi. Expedita voluptatum, alias temporibus voluptas quod aliquid officiis.</p>
  <div class="signup"><div class="field">email</div><div class="go">SIGN UP</div></div>
</section>

<div class="feature-img abs" role="img" aria-label="Photo of four sodalite angel carvings"></div>
<div class="thumb abs" role="img" aria-label="Photo of tiger eye angels" style="left:60px;background:linear-gradient(160deg,#c49a6e,#8a6440)"></div>
<div class="thumb abs" role="img" aria-label="Photo of rose quartz angels" style="left:161px;background:linear-gradient(160deg,#f6d2d9,#eaaab6)"></div>
<div class="thumb abs" role="img" aria-label="Photo of opalite angels" style="left:262px;background:linear-gradient(160deg,#f0f3f8,#d2dcea)"></div>
<div class="thumb abs" role="img" aria-label="Photo of green aventurine angels" style="left:363px;background:linear-gradient(160deg,#bddcc2,#8cb898)"></div>
<div class="thumb abs" role="img" aria-label="Photo of amethyst angels" style="left:464px;background:linear-gradient(160deg,#d2b6e0,#9a7ab6)"></div>

<div class="detail abs">
  <div class="rule"></div>
  <div class="name">Sample Name Here</div>
  <div class="rule"></div>
  <div class="reviews"><b>☆☆☆☆☆</b> No reviews</div>
  <div class="price">$70.00</div>
  <div class="copy">
    <p>Lorem ipsum dolor sit amet, consectetuer adipiscing elit, sed diam nonummy nibh euismod tincidunt ut laoreet dolore magna aliquam erat volutpat. Ut wisi enim ad minim veniam, quis nostrud exerci tation ullamcorper suscipit lobortis nisl ut aliquip ex ea commodo consequat. Duis autem vel eum iriure dolor in.</p>
    <p>Hendrerit in vulputate velit esse molestie consequat, vel illum dolore eu feugiat nulla facilisis at vero eros et accumsan et iusto odio dignissim qui blandit praesent luptatum zzril delenit augue duis dolore te feugait nulla facilisi. Lorem ipsum dolor sit amet, cons ectetuer adipiscing elit, sed diam nonummy nibh euismod tincidunt ut laoreet dolore magna aliquam erat volutpat. Ut wisi enim ad minim.</p>
    <p>Hendrerit in vulputate velit esse molestie consequat, vel illum dolore eu feugiat nulla facilisis at vero eros et accumsan et iusto odio dignissim qui blandit praesent luptatum zzril delenit augue duis dolore te feugait nulla facilisi. Lorem ipsum dolor sit amet, cons ectetuer adipiscing elit, sed diam nonummy nibh euismod tincidunt ut laoreet dolore magna aliquam erat volutpat.</p>
  </div>
</div>
<div class="add-cart abs">ADD TO CART</div>

<h2 class="section-title abs" style="left:48px;top:3228px">Blog Posts</h2>
<div class="row-arrow abs" style="left:1027px;top:3235px"><svg width="14" height="20"><path d="M12 2L3 10l9 8" fill="none" stroke="#fff" stroke-width="3"/></svg></div>
<div class="row-arrow abs" style="left:1094px;top:3235px"><svg width="14" height="20"><path d="M2 2l9 8-9 8" fill="none" stroke="#fff" stroke-width="3"/></svg></div>
<div class="blog-rule abs"></div>

<article class="post abs" style="left:48px"><div class="post-img" role="img" aria-label="Blog photo of crystal angel carvings"></div><h3>Sample title here</h3><div class="date">Posted by Admin · February 10, 2018</div><p class="excerpt">Lorem ipsum dolor sit amet, consectetuer adipiscing elit, sed diam nonummy nibh euismod tincidunt ut laoreet dolore magna aliquam erat volutpat. Ut wisi enim ad minim veniam, quis nostrud exerci tation ullamcorper suscipit lobortis nisl ut aliquip ex ea commodo consequat. Duis autem vel eum iriure dolor in hendrerit in vulputate velit esse molestie consequat, vel illum dolore eu feugiat nulla facilisis.</p></article>
<article class="post abs" style="left:423px"><div class="post-img" role="img" aria-label="Blog photo of crystal angel carvings"></div><h3>Sample title here</h3><div class="date">Posted by Admin · February 10, 2018</div><p class="excerpt">Lorem ipsum dolor sit amet, consectetuer adipiscing elit, sed diam nonummy nibh euismod tincidunt ut laoreet dolore magna aliquam erat volutpat. Ut wisi enim ad minim veniam, quis nostrud exerci tation ullamcorper suscipit lobortis nisl ut aliquip ex ea commodo consequat. Duis autem vel eum iriure dolor in hendrerit in vulputate velit esse molestie consequat, vel illum dolore eu feugiat nulla facilisis.</p></article>
<article class="post abs" style="left:798px"><div class="post-img" role="img" aria-label="Blog photo of crystal angel carvings"></div><h3>Sample title here</h3><div class="date">Posted by Admin · February 10, 2018</div><p class="excerpt">Lorem ipsum dolor sit amet, consectetuer adipiscing elit, sed diam nonummy nibh euismod tincidunt ut laoreet dolore magna aliquam erat volutpat. Ut wisi enim ad minim veniam, quis nostrud exerci tation ullamcorper suscipit lobortis nisl ut aliquip ex ea commodo consequat. Duis autem vel eum iriure dolor in hendrerit in vulputate velit esse molestie consequat, vel illum dolore eu feugiat nulla facilisis.</p></article>

<section class="testimonials abs" role="img" aria-label="Dim background photo of crystal carvings">
  <h2>Customer Testimonials</h2>
</section>
<div class="quote-box abs">
  Lorem ipsum dolor sit amet, consectetuer adipiscing elit, sed diam nonummy nibh euismod tincidunt ut laoreet dolore<br>
  Lorem ipsum dolor sit amet, consectetuer adipiscing elit, sed diam nonummy nibh euismod<br>
  Lorem ipsum dolor sit amet, consectetuer adipiscing elit, sed diam non
  <div class="who">~ Clara M. Hollis ~</div>
</div>
<div class="t-arrow abs" style="left:545px"><svg width="14" height="20"><path d="M12 2L3 10l9 8" fill="none" stroke="#fff" stroke-width="3"/></svg></div>
<div class="t-arrow abs" style="left:615px"><svg width="14" height="20"><path d="M2 2l9 8-9 8" fill="none" stroke="#fff" stroke-width="3"/></svg></div>

<footer class="footer abs">Copyright 2018 | <span>Company Here</span></footer>

</body>
</html>
```